Golden Lantern Take Away, take away menu

We want to use the double sided flyer design to produce a bulk amount of take away menus, which incorporate full contact details for our two shopfronts. We are a Take Away business in Wagga Wagga NSW, with two store, one which opened last year. We may also look to use these flyers for a letter box drop into the future. Our detailed menu can be found at goldenlanterntakeaway.com.au and contact details for both shops can be found on our facebook page Golden Lantern Take Away.

Hi all, Please note that the menu prices on our website are not the current prices. Please contact me with an email so I can send through a correct copy. I will be extending the due date to compensate for this oversight. Thanks.

Reason: Deadline is being extended as the old prices are still advertised on our menu (@goldenlanterntakeaway.com) . Please contact me via email for a copy of the up to date pricing.

Hi all, Please note that a file has been updated to the brief with current pricing. Please use this pricing in any proposals. Please don't use any of the combo deals in your proposals as they may be subject to change. Please also have a disclaimer at the bottom of your flyer that states "Please note: Prices may be subject to change". Sorry about the dripping of information as this is our first time using sketch hive. Thanks.

```html
<!DOCTYPE html>
<html lang="en">
<head>
<meta charset="utf-8">
<title>Golden Lantern Take Away – Menu Flyer</title>
<link href="https://fonts.googleapis.com/css2?family=Jost:ital,wght@0,400;0,500;0,600;0,700;1,500;1,600&display=swap" rel="stylesheet">
<style>
:root{
  --bg:#7a5638;
  --blue:#3461ad;
  --yellow:#e9e21a;
  --white:#ffffff;
  --ink:#121212;
  --red:#e0202a;
  --label:#f3ece4;
}
*{box-sizing:border-box;margin:0;padding:0}
html,body{width:1200px;height:880px;overflow:hidden}
body{background:var(--bg);font-family:"Jost",sans-serif;position:relative}
.side-label{position:absolute;top:34px;width:560px;text-align:center;color:var(--label);font-size:21px;font-weight:400;letter-spacing:.5px}
.flyer{position:absolute;top:80px;width:560px;height:765px;overflow:hidden;box-shadow:0 4px 14px rgba(0,0,0,.35)}
.flyer--front{left:40px}
.flyer--back{left:620px}
.flyer__bg{position:absolute;inset:0}
.tagline{position:absolute;top:16px;left:0;width:100%;text-align:center;color:var(--yellow);font-weight:600;font-size:17.5px}
.brand-title{position:absolute;top:60px;left:0;width:100%;text-align:center;color:var(--blue);font-weight:500;font-size:42px;letter-spacing:.2px}
.menu-col{position:absolute;top:147px;width:242px}
.menu-col--left{left:18px}
.menu-col--right{left:280px}
.section-head{background:var(--blue);color:var(--white);font-weight:700;font-size:29px;letter-spacing:1px;height:40px;line-height:42px;padding-left:8px;margin-bottom:8px}
.sub-head{color:var(--blue);font-weight:700;font-size:16px;letter-spacing:.5px;margin:6px 0 1px}
.menu-list{list-style:none}
.item{display:flex;align-items:baseline;font-size:14.6px;font-weight:600;color:var(--ink);line-height:20.8px}
.item__name{white-space:nowrap}
.item__name em{font-weight:500}
.item__dots{flex:1;border-bottom:1.5px dotted #555;margin:0 3px;transform:translateY(-3px);min-width:6px}
.item__price{white-space:nowrap}
.item-note{font-size:14.6px;font-weight:500;font-style:italic;color:var(--ink);line-height:18px}
.item-note--indent{padding-left:40px}
.promise{margin-top:16px;color:var(--red);font-style:italic;font-weight:500;font-size:13.2px;line-height:15.5px;text-align:justify}
.footer{position:absolute;left:0;top:640px;width:560px;height:125px}
.footer__badge{position:absolute;left:18px;top:5px;width:130px;height:40px;background:var(--white);display:flex;align-items:center;gap:4px;padding:0 5px;overflow:hidden}
.footer__badge-dot{width:10px;height:10px;border-radius:50%;background:var(--blue);flex:none}
.footer__badge-name{color:var(--blue);font-size:8.8px;font-weight:500;white-space:nowrap}
.footer__hours{position:absolute;left:20px;top:52px;color:var(--white);font-size:19px;font-weight:600}
.footer__social{position:absolute;left:165px;top:4px;display:flex;align-items:center;gap:6px;color:var(--yellow);font-size:18.5px;font-weight:600;white-space:nowrap}
.footer__social-square{width:16px;height:16px;background:var(--white);border-radius:2px;flex:none}
.shop{position:absolute;color:var(--white);font-weight:600;display:flex;flex-direction:column;gap:0}
.shop--one{left:165px;top:32px}
.shop--two{left:315px;top:32px}
.shop__line{display:flex;align-items:center;gap:5px;white-space:nowrap;font-size:17px;line-height:22px}
.shop__line--phone{font-size:19px;line-height:24px}
.shop__icon{width:12px;height:14px;flex:none}
.footer__note{position:absolute;left:18px;top:88px;width:526px;color:var(--yellow);font-size:12px;font-weight:600;line-height:15px}
</style>
</head>
<body>

<div class="side-label" style="left:40px">Front</div>
<div class="side-label" style="left:620px">Back</div>

<section class="flyer flyer--front">
  <svg class="flyer__bg" viewBox="0 0 560 765" width="560" height="765" aria-hidden="true">
    <rect width="560" height="765" fill="var(--yellow)"/>
    <path d="M0 0H560V48C420 60 160 32 0 52Z" fill="var(--blue)"/>
    <path d="M0 52C160 32 420 60 560 48V116C400 138 200 116 0 133Z" fill="var(--white)"/>
    <path d="M0 133C200 116 400 138 560 116" fill="none" stroke="var(--blue)" stroke-width="4"/>
    <path d="M0 628C180 604 380 640 560 618V765H0Z" fill="var(--blue)"/>
  </svg>
  <p class="tagline">Serving Wagga’s Best Take Away Food for over 35 Years!</p>
  <h1 class="brand-title">Golden Lantern Take Away</h1>

  <div class="menu-col menu-col--left">
    <h2 class="section-head">HOT FOOD</h2>
    <ul class="menu-list">
      <li class="item"><span class="item__name">Minimum Chips</span><span class="item__dots"></span><span class="item__price">$3.00</span></li>
      <li class="item"><span class="item__name">Dim Sim - Meat</span><span class="item__dots"></span><span class="item__price">$1.20</span></li>
      <li class="item"><span class="item__name">Dim Sim - Veggie</span><span class="item__dots"></span><span class="item__price">$1.30</span></li>
      <li class="item"><span class="item__name">Chook Roll</span><span class="item__dots"></span><span class="item__price">$2.60</span></li>
      <li class="item"><span class="item__name">Spring Roll</span><span class="item__dots"></span><span class="item__price">$2.60</span></li>
      <li class="item"><span class="item__name">Mini Spring Roll</span><span class="item__dots"></span><span class="item__price">$1.20</span></li>
      <li class="item"><span class="item__name">Chicken D/Stick</span><span class="item__dots"></span><span class="item__price">$3.00</span></li>
      <li class="item"><span class="item__name">Chicken Wing Ding</span><span class="item__dots"></span><span class="item__price">$1.40</span></li>
      <li class="item"><span class="item__name">Chicken Chippies <em>(10 pcs)</em></span><span class="item__dots"></span><span class="item__price">$2.00</span></li>
      <li class="item"><span class="item__name">Pineapple Fritter</span><span class="item__dots"></span><span class="item__price">$1.80</span></li>
      <li class="item"><span class="item__name">Chicken Nuggets</span><span class="item__dots"></span><span class="item__price">$0.80</span></li>
      <li class="item"><span class="item__name">Corn Jacks</span><span class="item__dots"></span><span class="item__price">$2.30</span></li>
      <li class="item"><span class="item__name">Corn Fritter</span><span class="item__dots"></span><span class="item__price">$0.80</span></li>
      <li class="item"><span class="item__name">Chicken Corn Roll</span><span class="item__dots"></span><span class="item__price">$2.50</span></li>
      <li class="item"><span class="item__name">Beef Croquets</span><span class="item__dots"></span><span class="item__price">$1.20</span></li>
      <li class="item"><span class="item__name">Chicken Garlic Balls</span><span class="item__dots"></span><span class="item__price">$1.30</span></li>
      <li class="item"><span class="item__name">Potato Scallops</span><span class="item__dots"></span><span class="item__price">$0.90</span></li>
      <li class="item"><span class="item__name">Potato Gems <em>(12 pcs)</em></span><span class="item__dots"></span><span class="item__price">$1.80</span></li>
      <li class="item"><span class="item__name">Battered Sav</span><span class="item__dots"></span><span class="item__price">$2.40</span></li>
    </ul>
  </div>

  <div class="menu-col menu-col--right">
    <h2 class="section-head">BURGERS</h2>
    <ul class="menu-list">
      <li class="item"><span class="item__name">Hamburger - Plain</span><span class="item__dots"></span><span class="item__price">$6.00</span></li>
      <li class="item"><span class="item__name">Hamburger - Egg</span><span class="item__dots"></span><span class="item__price">$6.50</span></li>
      <li class="item"><span class="item__name">Hamburger - Lot</span><span class="item__dots"></span><span class="item__price">$8.00</span></li>
      <li class="item"><span class="item__name">Cheese Burger</span><span class="item__dots"></span><span class="item__price">$5.50</span></li>
      <li class="item"><span class="item__name">Chicken Schnitzel - Plain</span><span class="item__dots"></span><span class="item__price">$7.00</span></li>
      <li class="item"><span class="item__name">Chicken Schnitzel - Lot</span><span class="item__dots"></span><span class="item__price">$9.00</span></li>
      <li class="item"><span class="item__name">Grilled Fish Burger</span><span class="item__dots"></span><span class="item__price">$8.50</span></li>
      <li class="item"><span class="item__name">Battered Fish Burger</span><span class="item__dots"></span><span class="item__price">$7.50</span></li>
      <li class="item"><span class="item__name">Prawn Burger</span><span class="item__dots"></span><span class="item__price">$6.00</span></li>
      <li class="item"><span class="item__name">Scallop Burger - Plain</span><span class="item__dots"></span><span class="item__price">$4.50</span></li>
      <li class="item"><span class="item__name">Scallop Burger - Lot</span><span class="item__dots"></span><span class="item__price">$6.50</span></li>
      <li class="item"><span class="item__name">Steak Sandwich - Plain</span><span class="item__dots"></span><span class="item__price">$7.00</span></li>
      <li class="item"><span class="item__name">Steak Sandwich - Lot</span><span class="item__dots"></span><span class="item__price">$9.00</span></li>
      <li class="item"><span class="item__name">Bacon &amp; Egg Roll</span><span class="item__dots"></span><span class="item__price">$6.00</span></li>
    </ul>
    <h3 class="sub-head" style="margin-top:8px">EXTRAS</h3>
    <ul class="menu-list">
      <li class="item"><span class="item__name">Pineapple</span><span class="item__dots"></span><span class="item__price">$0.50</span></li>
      <li class="item"><span class="item__name">Cheese</span><span class="item__dots"></span><span class="item__price">$0.50</span></li>
      <li class="item"><span class="item__name">Egg</span><span class="item__dots"></span><span class="item__price">$0.50</span></li>
      <li class="item"><span class="item__name">Salad <em>(Lettuce, Tomato,</em></span><span class="item__dots"></span><span class="item__price">$0.30</span></li>
    </ul>
    <p class="item-note item-note--indent">Beetroot - each)</p>
  </div>

  <footer class="footer">
    <div class="footer__badge"><span class="footer__badge-dot"></span><span class="footer__badge-name">Golden Lantern Take Away</span></div>
    <p class="footer__hours">7 days a week</p>
    <p class="footer__social"><span class="footer__social-square"></span>friendspace.com/GoldenLanternTakeAway</p>
    <div class="shop shop--one">
      <span class="shop__line"><svg class="shop__icon" viewBox="0 0 12 14"><path d="M6 0a4.5 4.5 0 0 0-4.5 4.5C1.5 8 6 14 6 14s4.5-6 4.5-9.5A4.5 4.5 0 0 0 6 0Zm0 6.3a1.8 1.8 0 1 1 0-3.6 1.8 1.8 0 0 1 0 3.6Z" fill="var(--red)"/></svg>42 Reed St</span>
      <span class="shop__line shop__line--phone"><svg class="shop__icon" viewBox="0 0 12 14"><path d="M2.6 1.2 4.4 3.6 3.4 5c.7 1.7 2 3 3.6 3.7l1.3-1 2.5 1.8-.9 2.2C6 11.6 1.2 6.8.6 2.2Z" fill="var(--red)"/></svg>69 555014</span>
    </div>
    <div class="shop shop--two">
      <span class="shop__line"><svg class="shop__icon" viewBox="0 0 12 14"><path d="M6 0a4.5 4.5 0 0 0-4.5 4.5C1.5 8 6 14 6 14s4.5-6 4.5-9.5A4.5 4.5 0 0 0 6 0Zm0 6.3a1.8 1.8 0 1 1 0-3.6 1.8 1.8 0 0 1 0 3.6Z" fill="var(--red)"/></svg>Shop 12 Lakeside Plaza</span>
      <span class="shop__line shop__line--phone"><svg class="shop__icon" viewBox="0 0 12 14"><path d="M2.6 1.2 4.4 3.6 3.4 5c.7 1.7 2 3 3.6 3.7l1.3-1 2.5 1.8-.9 2.2C6 11.6 1.2 6.8.6 2.2Z" fill="var(--red)"/></svg>69 555027</span>
    </div>
    <p class="footer__note">Offering Great options for morning "Smoko", lunch or Dinner. Phone orders are a great way to save time so feel free to call ahead. Please note: Prices may be subject to change.</p>
  </footer>
</section>

<section class="flyer flyer--back">
  <svg class="flyer__bg" viewBox="0 0 560 765" width="560" height="765" aria-hidden="true">
    <rect width="560" height="765" fill="var(--yellow)"/>
    <path d="M0 0H560V48C420 60 160 32 0 52Z" fill="var(--blue)"/>
    <path d="M0 52C160 32 420 60 560 48V116C400 138 200 116 0 133Z" fill="var(--white)"/>
    <path d="M0 133C200 116 400 138 560 116" fill="none" stroke="var(--blue)" stroke-width="4"/>
    <path d="M0 628C180 604 380 640 560 618V765H0Z" fill="var(--blue)"/>
  </svg>
  <p class="tagline">Serving Wagga’s Best Take Away Food for over 35 Years!</p>
  <h1 class="brand-title">Golden Lantern Take Away</h1>

  <div class="menu-col menu-col--left">
    <h2 class="section-head">SEAFOOD</h2>
    <ul class="menu-list">
      <li class="item"><span class="item__name">Fish - Battered</span><span class="item__dots"></span><span class="item__price">$6.50</span></li>
      <li class="item"><span class="item__name">Fish - Grilled</span><span class="item__dots"></span><span class="item__price">$7.00</span></li>
      <li class="item"><span class="item__name">Fish - Crumbed</span><span class="item__dots"></span><span class="item__price">$7.50</span></li>
      <li class="item"><span class="item__name">Fish - Cocktail</span><span class="item__dots"></span><span class="item__price">$1.30</span></li>
      <li class="item"><span class="item__name">Barramundi</span><span class="item__dots"></span><span class="item__price">$7.50</span></li>
      <li class="item"><span class="item__name">Grilled Fish &amp; Chips</span><span class="item__dots"></span><span class="item__price">$8.50</span></li>
      <li class="item"><span class="item__name">Grilled Fish &amp; Salad</span><span class="item__dots"></span><span class="item__price">$9.50</span></li>
      <li class="item"><span class="item__name">Grilled Fish, Salad &amp; Chips</span><span class="item__dots"></span><span class="item__price">$11.00</span></li>
      <li class="item"><span class="item__name">Barramundi &amp; Chips</span><span class="item__dots"></span><span class="item__price">$9.00</span></li>
      <li class="item"><span class="item__name">Barramundi &amp; Salad</span><span class="item__dots"></span><span class="item__price">$10.00</span></li>
      <li class="item"><span class="item__name">Barramundi, Salad &amp; Chips</span><span class="item__dots"></span><span class="item__price">$11.50</span></li>
    </ul>
    <h3 class="sub-head" style="margin-top:10px">SEAFOOD BASKET</h3>
    <ul class="menu-list">
      <li class="item"><span class="item__name">Fish Cake</span><span class="item__dots"></span><span class="item__price">$2.80</span></li>
      <li class="item"><span class="item__name">Prawn Cutlet</span><span class="item__dots"></span><span class="item__price">$2.20</span></li>
      <li class="item"><span class="item__name">Island Scallop</span><span class="item__dots"></span><span class="item__price">$1.50</span></li>
      <li class="item"><span class="item__name">Calamari Rings</span><span class="item__dots"></span><span class="item__price">$0.80</span></li>
      <li class="item"><span class="item__name">Sea Shanties</span><span class="item__dots"></span><span class="item__price">$1.20</span></li>
      <li class="item"><span class="item__name">Prawn Bar</span><span class="item__dots"></span><span class="item__price">$2.50</span></li>
      <li class="item"><span class="item__name">Seafood Stick</span><span class="item__dots"></span><span class="item__price">$2.30</span></li>
    </ul>
  </div>

  <div class="menu-col menu-col--right">
    <h2 class="section-head">SANDWICHES</h2>
    <h3 class="sub-head" style="margin-top:4px">TOASTED</h3>
    <ul class="menu-list">
      <li class="item"><span class="item__name">Cheese</span><span class="item__dots"></span><span class="item__price">$3.00</span></li>
      <li class="item"><span class="item__name">Cheese &amp; Tomato</span><span class="item__dots"></span><span class="item__price">$3.50</span></li>
      <li class="item"><span class="item__name">Ham &amp; Cheese</span><span class="item__dots"></span><span class="item__price">$4.50</span></li>
      <li class="item"><span class="item__name">Ham, Cheese &amp; Tomato</span><span class="item__dots"></span><span class="item__price">$5.00</span></li>
    </ul>
    <h3 class="sub-head" style="margin-top:8px">FRESH</h3>
    <ul class="menu-list">
      <li class="item"><span class="item__name">Cheese</span><span class="item__dots"></span><span class="item__price">$2.50</span></li>
      <li class="item"><span class="item__name">Cheese &amp; Tomato</span><span class="item__dots"></span><span class="item__price">$3.00</span></li>
      <li class="item"><span class="item__name">Ham &amp; Cheese</span><span class="item__dots"></span><span class="item__price">$4.00</span></li>
      <li class="item"><span class="item__name">Salad <em>(inc Cheese &amp; Mayo)</em></span><span class="item__dots"></span><span class="item__price">$4.50</span></li>
      <li class="item"><span class="item__name">Ham, Cheese &amp; Salad</span><span class="item__dots"></span><span class="item__price">$5.50</span></li>
    </ul>
    <p class="item-note">(inc Mayo)</p>
    <h3 class="sub-head" style="margin-top:8px">ROLLS</h3>
    <ul class="menu-list">
      <li class="item"><span class="item__name">Salad <em>(inc Cheese &amp; Mayo)</em></span><span class="item__dots"></span><span class="item__price">$5.00</span></li>
      <li class="item"><span class="item__name">Ham, Cheese &amp; Salad</span><span class="item__dots"></span><span class="item__price">$6.00</span></li>
    </ul>
    <p class="item-note">(inc Mayo)</p>
    <p class="promise">We would welcome the opportunity to earn your trust and deliver you the best Take Away Food in the industry.</p>
  </div>

  <footer class="footer">
    <div class="footer__badge"><span class="footer__badge-dot"></span><span class="footer__badge-name">Golden Lantern Take Away</span></div>
    <p class="footer__hours">7 days a week</p>
    <p class="footer__social"><span class="footer__social-square"></span>friendspace.com/GoldenLanternTakeAway</p>
    <div class="shop shop--one">
      <span class="shop__line"><svg class="shop__icon" viewBox="0 0 12 14"><path d="M6 0a4.5 4.5 0 0 0-4.5 4.5C1.5 8 6 14 6 14s4.5-6 4.5-9.5A4.5 4.5 0 0 0 6 0Zm0 6.3a1.8 1.8 0 1 1 0-3.6 1.8 1.8 0 0 1 0 3.6Z" fill="var(--red)"/></svg>42 Reed St</span>
      <span class="shop__line shop__line--phone"><svg class="shop__icon" viewBox="0 0 12 14"><path d="M2.6 1.2 4.4 3.6 3.4 5c.7 1.7 2 3 3.6 3.7l1.3-1 2.5 1.8-.9 2.2C6 11.6 1.2 6.8.6 2.2Z" fill="var(--red)"/></svg>69 555014</span>
    </div>
    <div class="shop shop--two">
      <span class="shop__line"><svg class="shop__icon" viewBox="0 0 12 14"><path d="M6 0a4.5 4.5 0 0 0-4.5 4.5C1.5 8 6 14 6 14s4.5-6 4.5-9.5A4.5 4.5 0 0 0 6 0Zm0 6.3a1.8 1.8 0 1 1 0-3.6 1.8 1.8 0 0 1 0 3.6Z" fill="var(--red)"/></svg>Shop 12 Lakeside Plaza</span>
      <span class="shop__line shop__line--phone"><svg class="shop__icon" viewBox="0 0 12 14"><path d="M2.6 1.2 4.4 3.6 3.4 5c.7 1.7 2 3 3.6 3.7l1.3-1 2.5 1.8-.9 2.2C6 11.6 1.2 6.8.6 2.2Z" fill="var(--red)"/></svg>69 555027</span>
    </div>
    <p class="footer__note">Offering Great options for morning "Smoko", lunch or Dinner. Phone orders are a great way to save time so feel free to call ahead. Please note: Prices may be subject to change.</p>
  </footer>
</section>

</body>
</html>
```